Sports Hatchback Wrap - Attract Attention

Please design a wrap with logos for a company car - 2020 Tarvo Lumen Swift Cruiser Hatchback, images attached.

We would like the design to attract attention and turn heads - perhaps something sporty, like racing stripes. We would also like to have some text - content - as opposed to just graphics and logo everywhere.

Vehicle is the Tarvo Lumen Harchback Swift Cruiser

Please use exact hex code colors of 3f9ed7 and 595959

Logo text font is the Aristocrat font

The remaining area where there is no graphics or font will be clear, to showcase the white diamond sparking paint beneath. We would like the car to remain more than 50% white (paint underneath) showing.

Also would like to see 2 blue racing stripes going down car hood and roof front to back on entite vehicle as part of the design...as one option. And if no racing stripes...inlike a full color front hood with a white logo as another option...like a PELMOR. I like blue accent pieces like small ones in the grill.

Also would like it to be not so busy....a bit more on the simplistic side but still eye catching.

Also no plain text on windows. Color skin is ok on windows but plain text on windows looks tacky. Prefer text on back bumper or harfhback door of car and design on sides of car.

Also like full main logo on front doors of car on both sides

Target Market(s)

Engineering and Architecture Companies

Industry/Entity Type

Engineering Consultant

Font styles to use
Serif
Other font styles liked:
• fonts MUST match the logo

Colors
33a6d7

Requirements
Must have
• There needs to be text in some visible parts of the car - perhaps the sides or the back. It should say:
"Drafting • Staffing • Training"
"qelplanwork.example"
"555-014-2736"
And the Chatterly, Snapvale, Quipster and WorkNexa logos
Nice to have
• I would like to incorporate sporty graphics into the design - perhaps racing strips, or bright blue trim around the car. We would also like to have the logo (or parts of the logo) visible from every angle - on the hood, roof, sides. The logo can be just the head, the head and text (QEL Planwork), or just the text - feel free to put pieces wherever they will fit.

Less is more - a cleaner minimalistic design will bring more attention to the logo.
Should not have
• No colors other than blue, grey, black, and white - the colors of the logo.

```html
<!DOCTYPE html>
<html lang="en">
<head>
<meta charset="utf-8">
<title>QEL Planwork – Hatchback Wrap, Left Side</title>
<link rel="stylesheet" href="https://fonts.googleapis.com/css2?family=Russo+One&family=Tinos&display=swap">
<style>
  :root {
    --brand-blue: #3f9ed7;
    --brand-grey: #595959;
    --panel-black: #0d0d0d;
    --icon-dark: #333333;
    --tab-grey: #3d4043;
    --paper: #ffffff;
  }
  html, body {
    margin: 0;
    padding: 0;
    width: 1200px;
    height: 800px;
    overflow: hidden;
    background: var(--paper);
  }
  .wrap-side {
    display: block;
    width: 1200px;
    height: 800px;
  }
  .band-top { fill: var(--brand-blue); }
  .panel-lower { fill: var(--panel-black); }
  .web-address {
    font-family: "Russo One", sans-serif;
    font-style: oblique;
    font-size: 44px;
    fill: var(--brand-grey);
  }
  .services {
    font-family: "Russo One", sans-serif;
    font-style: oblique;
    font-size: 46px;
    fill: var(--brand-blue);
  }
  .phone {
    font-family: "Russo One", sans-serif;
    font-style: oblique;
    font-size: 32px;
    fill: var(--brand-blue);
  }
  .social-dot { fill: var(--icon-dark); }
  .social-name {
    font-family: "Russo One", sans-serif;
    font-size: 12px;
    fill: var(--icon-dark);
  }
  .brand-name {
    font-family: "Russo One", sans-serif;
    font-size: 64px;
    fill: var(--brand-blue);
  }
  .brand-mark { fill: var(--brand-blue); }
  .streak { fill: var(--brand-blue); }
  .trace { fill: none; stroke: var(--brand-blue); stroke-width: 1.5; opacity: 0.45; }
  .side-tab { fill: var(--tab-grey); }
  .side-tab-label {
    font-family: "Tinos", serif;
    font-size: 30px;
    fill: var(--paper);
  }
</style>
</head>
<body>
<svg class="wrap-side" viewBox="0 0 1200 800" xmlns="http://www.w3.org/2000/svg">
  <defs>
    <linearGradient id="streak-fade" x1="0" y1="0" x2="1" y2="0">
      <stop offset="0" stop-color="#3f9ed7" stop-opacity="0.05"/>
      <stop offset="0.6" stop-color="#3f9ed7" stop-opacity="0.55"/>
      <stop offset="1" stop-color="#3f9ed7" stop-opacity="0.15"/>
    </linearGradient>
  </defs>

  <!-- upper blue band with web address -->
  <polygon class="band-top" points="0,185 669,0 897,0 0,292"/>
  <text class="web-address" transform="translate(114 214) rotate(-19)" textLength="470">qelplanwork.example</text>

  <!-- social network names -->
  <g class="social-row" transform="translate(52 122) rotate(-19)">
    <circle class="social-dot" cx="0" cy="0" r="9"/>
    <text class="social-name" x="13" y="4">Chatterly</text>
    <circle class="social-dot" cx="80" cy="0" r="9"/>
    <text class="social-name" x="93" y="4">Snapvale</text>
    <circle class="social-dot" cx="158" cy="0" r="9"/>
    <text class="social-name" x="171" y="4">Quipster</text>
    <circle class="social-dot" cx="236" cy="0" r="9"/>
    <text class="social-name" x="249" y="4">WorkNexa</text>
  </g>

  <!-- main brand name -->
  <g class="brand-lockup">
    <rect class="brand-mark" x="388" y="236" width="28" height="28"/>
    <text class="brand-name" x="432" y="272">QEL Planwork</text>
  </g>

  <!-- lower black panel -->
  <polygon class="panel-lower" points="0,705 1200,282 1200,800 0,800"/>

  <!-- light streaks inside the black panel -->
  <g class="streaks" transform="translate(760 600) rotate(-19)">
    <rect class="trace" x="-380" y="-60" width="820" height="260"/>
    <rect class="trace" x="-40" y="-110" width="330" height="22"/>
    <rect class="streak" x="60" y="-84" width="250" height="26" fill="url(#streak-fade)"/>
    <rect class="streak" x="20" y="-50" width="520" height="60" fill="url(#streak-fade)"/>
    <rect class="streak" x="-120" y="40" width="700" height="46" fill="url(#streak-fade)"/>
    <rect class="streak" x="80" y="120" width="560" height="80" fill="url(#streak-fade)"/>
    <rect class="streak" x="-300" y="210" width="900" height="40" fill="url(#streak-fade)"/>
    <rect class="streak" x="-20" y="-60" width="14" height="26" opacity="0.7"/>
    <rect class="streak" x="0" y="-62" width="22" height="30" opacity="0.5"/>
  </g>

  <!-- services line and phone -->
  <text class="services" transform="translate(245 676) rotate(-19)" textLength="790">Drafting • Staffing • Training</text>
  <text class="phone" transform="translate(453 707) rotate(-19)" textLength="306">555-014-2736</text>

  <!-- side marker tab -->
  <rect class="side-tab" x="0" y="398" width="64" height="183"/>
  <text class="side-tab-label" transform="translate(22 424) rotate(90)">left Side</text>
</svg>
</body>
</html>
```